clearfern website

I need the graphics and images created for a web site. I have settled on a layout but are open to alternatives

I have already purchased the images I want to use.

I want the graphics/design to really give the web site a lift without deviating from the core concept (which is lots of white space, clean looking)

I have further files to upload for use (another 4).

The link to the current web site that requires re-skinning is: http://www.talvinpromo.com.au/cgi-bin/xmlweb.cgi/scriptlet/clearfern?cms_section=clearfern&cms_name=home
Updates

I forgot to mention that I would the design elements of the various text boxes down the right hand side and along the bottom of the page to be improved.  At the moment they look very one dimensional and boring.

Thanks

All files have now been uploaded.

Hi Guys
Some great designs are coming through.  I thought I would share elements that I like for each for those of you who are prepared to tweek their submissions.

Design ID 27087
1. Used used the proper logo file supplied
2. Like the use of images and design of the various text boxes down the right hand side of the page
3.  I like the footer - but would maybe change some of the images used
4.  I like the navigation bar

Design ID 27265
1. Like the placement of icons up the top.  I think this concept would work if there were maybe three other icons up there as well

Design ID 27266
1.  Like the design elements of the various text boxes down the right hand side of the page
2.  Like the grey background strip down the right hand side of page

Key thing I would like improved:
1.  The style and use of text in the header/banner.  I also think it looks a little one dimensional

Thanks

Rgds
Derek

Target Market(s)

SME businesses

Number of Pages Required

1 page

Requirements
Must have
• 1. Header/Banner must replicate concept provided
2. Please check out this web site as it is the design inspiration and should heavily influence the final design (use of colour etc) - www.plomwickstudio.com

```html
<!DOCTYPE html>
<html lang="en">
<head>
<meta charset="utf-8">
<title>clearfern marketing</title>
<link href="https://fonts.googleapis.com/css2?family=Merriweather:wght@400;700&family=Source+Serif+4:wght@400;600;700&family=Arimo:wght@400;700&display=swap" rel="stylesheet">
<style>
:root{
  --blue:#0a72c4;
  --blue-deep:#0b5aa8;
  --navy:#1a2a4a;
  --text:#555;
  --grey:#e0e0e0;
  --strip:#dcdcdc;
  --white:#fff;
}
*{margin:0;padding:0;box-sizing:border-box}
html,body{width:730px;height:1200px;overflow:hidden;background:var(--white)}
body{position:relative;font-family:'Source Serif 4',Georgia,serif;color:var(--text)}
.abs{position:absolute}
.logo{left:25px;top:22px;display:flex;align-items:center;gap:6px;font-family:'Source Serif 4',serif;font-weight:700;font-size:27px;color:var(--blue)}
.logo .dot{width:22px;height:22px;border-radius:50%;background:var(--blue)}
.nav{left:0;top:37px;width:730px;font-family:'Arimo',sans-serif;font-size:9.5px;font-weight:700;color:#555}
.nav span{position:absolute;top:0;padding:3px 4px;white-space:nowrap}
.nav .active{background:#ccc}
.strip{left:0;width:730px;height:9px;background:var(--strip)}
.banner{left:0;top:80px;width:730px;height:251px;background:linear-gradient(160deg,#3f6fcf 0%,#7aa3e0 45%,#dfe9f6 75%,#9bb8e6 100%)}
.banner h1{position:absolute;left:30px;top:52px;font-family:'Merriweather',serif;font-weight:700;font-size:35px;letter-spacing:2px;color:var(--white)}
.banner .sub{position:absolute;left:29px;top:104px;font-family:'Merriweather',serif;font-size:13px;line-height:16px;letter-spacing:2.3px;color:var(--navy)}
.banner .call{position:absolute;left:30px;top:165px;display:flex;align-items:center;gap:6px;font-family:'Source Serif 4',serif;font-weight:700;font-size:21px;color:var(--white)}
.icon-ph{position:absolute;background:#2c4aa3}
.globe{left:459px;top:34px;width:92px;height:92px;border-radius:50%;background:radial-gradient(circle at 40% 35%,#6f95e8,#1f3a9a)}
.tv{left:465px;top:160px;width:84px;height:65px;border-radius:10px;background:#2c4aa3}
.tag{position:absolute;width:160px;text-align:center;font-family:'Merriweather',serif;font-weight:700;font-size:17px;line-height:19px;color:var(--white);text-shadow:0 1px 2px rgba(0,0,0,.35)}
.intro{left:23px;top:366px;width:410px;font-size:11px;line-height:14px}
.intro h2{font-size:11px;font-weight:700;color:var(--blue);margin-bottom:14px}
.intro p{margin-bottom:14px}
.divider{left:452px;top:384px;height:705px;border-left:1px dotted #999}
.service{left:37px;width:400px;height:85px}
.service .pic{position:absolute;left:0;top:0;width:135px;height:80px;border-radius:10px;border:1px solid #ccc;background:linear-gradient(#f7f7f7,#e4e4e4)}
.service h3{position:absolute;left:146px;top:0;font-weight:600;font-size:17px;color:var(--blue);white-space:nowrap}
.service p{position:absolute;left:146px;top:22px;width:254px;font-size:11px;line-height:14px;color:#333}
.service a{position:absolute;left:146px;top:68px;font-size:11px;font-weight:700;color:#222;text-decoration:none}
.box{left:483px;width:208px;background:var(--grey)}
.box .head{position:absolute;left:0;top:0;width:208px;height:27px;background:var(--blue);color:var(--white);font-size:10.5px;font-weight:700;text-align:center;line-height:27px}
.box .tail{position:absolute;left:6px;top:27px}
.box .body{position:absolute;left:24px;top:52px;width:180px;font-size:11px;line-height:14.5px;color:#333}
.box .rule{position:absolute;left:3px;width:202px;border-top:1px dotted #888}
.list{left:15px !important;top:45px !important;line-height:14px}
.list div{margin-bottom:7px}
.video{position:absolute;left:13px;top:47px;width:183px;height:100px;border-radius:8px;border:1px solid #ccc;background:var(--white)}
.video .bar{position:absolute;left:0;bottom:12px;width:100%;height:10px;background:#e2e2e2}
.footer{left:0;top:1116px;width:730px;height:33px;background:linear-gradient(90deg,#0b3f94,#0a7bc8)}
.foot-text{top:1154px;font-size:11px;color:#333}
.foot-text b{color:var(--blue)}
</style>
</head>
<body>
<header>
  <div class="abs logo"><span class="dot"></span>clearfern</div>
  <nav class="abs nav">
    <span class="active" style="left:259px">HOME</span>
    <span style="left:315px">WHAT WE'RE WORKING ON</span>
    <span style="left:463px">ABOUT US</span>
    <span style="left:536px">MEDIA</span>
    <span style="left:594px">BLOG</span>
    <span style="left:647px">CONTACT</span>
  </nav>
</header>
<div class="abs strip" style="top:71px"></div>
<section class="abs banner" role="img" aria-label="Sunny blue sky with clouds">
  <h1>Reshaping Business</h1>
  <div class="sub">clearfern is a marketing agency specialising<br>in marketing campaign design &amp; execution using<br>traditional and digital media</div>
  <div class="call">
    <svg width="16" height="34" viewBox="0 0 16 34"><rect x="1" y="1" width="14" height="32" rx="3" fill="#2c4aa3" stroke="#fff" stroke-width="1"/><rect x="3" y="4" width="10" height="8" fill="#fff"/><g fill="#fff"><circle cx="5" cy="17" r="1"/><circle cx="8" cy="17" r="1"/><circle cx="11" cy="17" r="1"/><circle cx="5" cy="22" r="1"/><circle cx="8" cy="22" r="1"/><circle cx="11" cy="22" r="1"/><circle cx="5" cy="27" r="1"/><circle cx="8" cy="27" r="1"/><circle cx="11" cy="27" r="1"/></g></svg>
    Call Now on 1300 555 014
  </div>
  <div class="icon-ph globe" role="img" aria-label="Glossy globe icon"></div>
  <div class="icon-ph tv" role="img" aria-label="Television icon"></div>
  <div class="tag" style="left:552px;top:63px">Online Digital<br>Solutions</div>
  <div class="tag" style="left:552px;top:170px">Video<br>Production</div>
</section>
<div class="abs strip" style="top:331px"></div>

<main>
  <div class="abs intro">
    <h2>At clearfern marketing we're reshaping business and building brands.</h2>
    <p>We're helping businesses like yours build their customer base and penetrate new markets. Clearfern achieve this through strategic market campaign design and execution using a combination of traditional and digital media.</p>
    <p>We're your outsourced marketing department.<br>As your outsourced marketing managers, clearfern specialise in providing marketing strategies, brand &amp; logo development, public relations campaigns, advertising strategies, social media strategies, web site design and online marketing strategies.</p>
    <p>We cause gravity to your business.</p>
    <p>We'll reposition your business in the marketplace so that it resonates with your target market. We'll then help you implement powerful online and offline lead generation and sales strategies.</p>
  </div>
  <div class="abs divider"></div>

  <div class="abs service" style="top:618px">
    <div class="pic" role="img" aria-label="Photo of two businessmen" style="background:linear-gradient(#c9c2b5,#8a8578)"></div>
    <h3>Marketing &amp; PR Strategy</h3>
    <p>Learn more about how we can help build your customer base and penetrate new markets.</p>
    <a href="#">Click here to find out more...</a>
  </div>
  <div class="abs service" style="top:738px">
    <div class="pic" role="img" aria-label="Darts in a target"></div>
    <h3>Campaign Design &amp; Execution</h3>
    <p>Seeking a marketing plan that works? Learn more about how we implement our powerful marketing strategies.</p>
    <a href="#">Click here to find out more...</a>
  </div>
  <div class="abs service" style="top:864px">
    <div class="pic" role="img" aria-label="Light bulb with at sign"></div>
    <h3>Campaign Design &amp; Execution</h3>
    <p>Seeking a marketing plan that works? Learn more about how we implement our powerful marketing strategies.</p>
    <a href="#">Click here to find out more...</a>
  </div>
  <div class="abs service" style="top:992px">
    <div class="pic" role="img" aria-label="Illustrated businessman with speech bubble"></div>
    <h3>Campaign Design &amp; Execution</h3>
    <p>Seeking a marketing plan that works? Learn more about how we implement our powerful marketing strategies.</p>
    <a href="#">Click here to find out more...</a>
  </div>
</main>

<aside>
  <div class="abs box" style="top:363px;height:180px">
    <div class="head">FREE MARKETING ASSESMENT</div>
    <svg class="tail" width="14" height="12"><path d="M0 0H14L2 12Z" fill="#0a72c4"/></svg>
    <div class="body" style="top:52px">At vero eos et accusam et justo duo dolores et ea rebum. Stet clita kasd gubergren, no</div>
    <div class="rule" style="top:101px"></div>
    <div class="body" style="top:111px">sea takimata sanctus est Lorem ipsum dolor sit amet. Lorem ipsum dolor sit amet, consetetu.</div>
  </div>
  <div class="abs box" style="top:555px;height:180px">
    <div class="head">JOIN OUR MAILING LIST</div>
    <svg class="tail" width="14" height="12"><path d="M0 0H14L2 12Z" fill="#0a72c4"/></svg>
    <div class="body" style="top:52px">At vero eos et accusam et justo duo dolores et ea rebum. Stet clita kasd gubergren, no</div>
    <div class="rule" style="top:101px"></div>
    <div class="body" style="top:111px">sea takimata sanctus est Lorem ipsum dolor sit amet. Lorem ipsum dolor sit amet, consetetu.</div>
  </div>
  <div class="abs box" style="top:748px;height:180px">
    <div class="head">WHAT ARE YOU LOOKING FOR?</div>
    <svg class="tail" width="14" height="12"><path d="M0 0H14L2 12Z" fill="#0a72c4"/></svg>
    <div class="body list" style="width:190px">
      <div>I want to increase brand awareness.</div>
      <div>I want greater lead generation.</div>
      <div>I want a powerful online strategy</div>
      <div style="line-height:11px">I want to launch a new product or service.</div>
      <div>I want a marketing overhaul.</div>
    </div>
    <div class="rule" style="top:164px"></div>
  </div>
  <div class="abs box" style="top:940px;height:164px">
    <div class="head">VIDCAST</div>
    <svg class="tail" width="14" height="12"><path d="M0 0H14L2 12Z" fill="#0a72c4"/></svg>
    <div class="video">
      <svg style="position:absolute;left:76px;top:30px" width="22" height="22"><circle cx="11" cy="11" r="10" fill="#ddd" stroke="#999"/><path d="M8 6L16 11L8 16Z" fill="#777"/></svg>
      <div class="bar"></div>
    </div>
  </div>
</aside>

<footer>
  <div class="abs footer"></div>
  <div class="abs foot-text" style="left:34px"><b>Site Map</b></div>
  <div class="abs foot-text" style="left:394px"><sup style="color:var(--blue);font-size:6px">©</sup> <b>clearfern</b>(02) 9555 0148 &nbsp; * &nbsp; Location: Sydney Australia</div>
</footer>
</body>
</html>
```